Scaffold Business needs new Email Signature

We are looking to change our email signatures. Something very Unique, modern and creative. the signatures should entail
- Employee name
- Title
- main phone
- call phone
- fax number
- website
- mail address
- Quibra review button (unique not the same you see everywhere)
- our logo banner (see attached)
- our 60th anniversary logo (see attached)
- Option to add employee picture and social media tab (proflume)
we really are looking for something that is very different from the rest.
open to having interactive options as well.

```html
<!DOCTYPE html>
<html lang="en">
<head>
<meta charset="utf-8">
<title>Bastion Equipment — Email Signature</title>
<link rel="stylesheet" href="https://fonts.googleapis.com/css2?family=Inter:wght@400;500;600;700;800&display=swap">
<style>
  :root {
    --page-bg: #e5e5e5;
    --card-bg: #ffffff;
    --ink: #2b2d33;
    --ink-soft: #3a3c42;
    --muted: #8d8e93;
    --brand-red: #8a1a16;
    --badge-tint: #a63a35;
    --band-bg: #f3f3f3;
    --rule: #dcdcdc;
    --star: #e5b31c;
    --link: #1479b8;
    --social: #0a75b5;
    --photo-a: #c9c3ba;
    --photo-b: #5a4438;
  }
  * { box-sizing: border-box; margin: 0; padding: 0; }
  html, body { width: 1018px; height: 1200px; overflow: hidden; }
  body { background: var(--page-bg); font-family: "Inter", Arial, sans-serif; color: var(--ink); position: relative; }

  .signature {
    position: absolute; left: 254px; top: 365px; width: 509px; height: 471px;
    background: var(--card-bg);
    box-shadow: 0 14px 30px rgba(0,0,0,.22);
  }
  .portrait {
    position: absolute; left: 57px; top: 85px; width: 93px; height: 93px; border-radius: 50%;
    background: radial-gradient(circle at 50% 45%, var(--photo-b) 0 34%, var(--photo-a) 36%);
  }
  .employee-name { position: absolute; left: 57px; top: 186px; font-size: 22px; font-weight: 700; letter-spacing: -.2px; }
  .employee-title { position: absolute; left: 57px; top: 213px; font-size: 10px; color: var(--ink-soft); }

  .contact { position: absolute; left: 268px; top: 85px; }
  .contact-item { margin-bottom: 6px; }
  .contact-label { display: block; font-size: 7.5px; font-weight: 700; color: var(--brand-red); text-transform: uppercase; line-height: 10px; }
  .contact-value { display: block; font-size: 13.5px; color: var(--ink); line-height: 19px; }
  .contact-item--email .contact-value { margin-top: 2px; }

  .brand-band {
    position: absolute; left: 40px; top: 243px; width: 424px; height: 68px; background: var(--band-bg);
  }
  .brand-name {
    position: absolute; left: 17px; top: 26px; font-size: 11px; font-weight: 700; color: var(--ink-soft);
    text-transform: uppercase; letter-spacing: .2px; display: flex; align-items: center; gap: 6px;
  }
  .brand-mark { width: 10px; height: 10px; background: var(--brand-red); }
  .band-divider { position: absolute; left: 175px; top: 21px; width: 1px; height: 26px; background: var(--rule); }
  .website { position: absolute; left: 194px; top: 27px; font-size: 12px; font-weight: 600; color: var(--muted); }
  .anniversary {
    position: absolute; right: 0; top: 0; width: 71px; height: 68px; background: var(--brand-red);
    display: flex; align-items: center; justify-content: center;
  }
  .anniversary-seal { width: 46px; height: 46px; border-radius: 50%; background: var(--badge-tint); }

  .reviews {
    position: absolute; left: 40px; top: 316px; width: 424px; height: 41px;
    border-top: 2px solid #e6e6e6; border-bottom: 2px solid #e6e6e6; display: flex;
  }
  .reviews-title {
    width: 200px; border-right: 2px solid #e6e6e6; display: flex; align-items: center; gap: 9px; padding-left: 17px;
    font-size: 15px; font-weight: 700; color: var(--ink-soft); text-transform: uppercase;
  }
  .reviews-dot { width: 20px; height: 20px; border-radius: 50%; background: var(--brand-red); }
  .reviews-score { display: flex; align-items: center; padding-left: 13px; font-size: 10px; color: var(--ink-soft); gap: 8px; }
  .reviews-score strong { font-weight: 600; }

  .social { position: absolute; left: 57px; top: 371px; display: flex; align-items: center; gap: 9px; }
  .social-badge { width: 24px; height: 24px; background: var(--social); }
  .social-link { font-size: 12.5px; color: var(--link); text-decoration: underline; }
</style>
</head>
<body>
  <div class="signature">
    <div class="portrait" role="img" aria-label="Employee portrait photo"></div>
    <h1 class="employee-name">Marla Quinn</h1>
    <p class="employee-title">Sales &amp; Marketing Director</p>

    <div class="contact">
      <div class="contact-item"><span class="contact-label">Main phone</span><span class="contact-value">555 214 3080</span></div>
      <div class="contact-item"><span class="contact-label">Call phone</span><span class="contact-value">+1 800 555 0143</span></div>
      <div class="contact-item"><span class="contact-label">Fax number</span><span class="contact-value">555 319 0172</span></div>
      <div class="contact-item contact-item--email"><span class="contact-label">Email</span><span class="contact-value">info@bastionscaffold.ca</span></div>
    </div>

    <div class="brand-band">
      <div class="brand-name"><span class="brand-mark"></span>Bastion Equipment</div>
      <div class="band-divider"></div>
      <div class="website">www.bastionscaffold.ca</div>
      <div class="anniversary" role="img" aria-label="60th anniversary badge">
        <span class="anniversary-seal"></span>
      </div>
    </div>

    <div class="reviews">
      <div class="reviews-title"><span class="reviews-dot"></span>Quibra Reviews</div>
      <div class="reviews-score">
        <svg width="15" height="15" viewBox="0 0 24 24"><path d="M12 2l2.9 6.6 7.1.6-5.4 4.7 1.6 7L12 17.3 5.8 21l1.6-7L2 9.2l7.1-.6z" fill="var(--star)"/></svg>
        <strong>4.4 Rating</strong><span>31 People reviews</span>
      </div>
    </div>

    <div class="social">
      <span class="social-badge"></span>
      <a class="social-link" href="#">Proflume profile</a>
    </div>
  </div>
</body>
</html>
```